New Business Cards for Restaurants

I am in need of Business cards for two of our restaurants. On the back of the cards I would like info about the other properties that we have so that people know we own other things in town.

Harbor Business card include the following: Name: Dana Pruitt, Phone Number: 850-318-4672, Email:Dana@harborlampkitchen.example, Resturant logo: Prefer the circle one, website address: www.harborlampkitchen.example. On the back side I would like at the top it to say Keystone Ventures, LLC. on another line underneath: Concepts by Dana Pruitt. Then the Pell logo in a circle, Rook logo in a circle and in plain lettering The Pruitt Room in a circle. Underneath each circle should be the address for each property. Pell address is : 1480 W Larkin Ave. Rook address is : 1476 W Larkin Ave and the Pruitt Room need to say "Coming Soon".

Pell and Rook card should be the reverse of Harbor's. Pell and Rook's logo on the front. with Pell address. Phone number on this one is 850-492-3106. Same email from above. On the back side should have the Keystone Ventures etc. Then Concepts by dana. Then Harbor's logo in a circle and the Pruitt Room in a circle.

When I say a circle I am thinking similar to the social media circle logos at the bottom of most websites .

Contact Information for Business Card

Font styles to use
Script

Requirements
Must have
• I would like the logos of the other properties on back to be in circles with their address underneath the circle.

```html
<!DOCTYPE html>
<html lang="en">
<head>
<meta charset="utf-8">
<title>Keystone Ventures – Business Cards</title>
<link rel="stylesheet" href="https://fonts.googleapis.com/css2?family=Libre+Baskerville:wght@400;700&family=Dancing+Script:wght@600&display=swap">
<style>
  :root {
    --bg: #3a302c;
    --card: #0b0b0c;
    --gold: #f0b81a;
    --logo-gold: #d9bd72;
    --white: #f2f2f2;
    --ink: #1a1a1a;
    --disc: #f4f4f4;
    --ring: #c9a55a;
  }
  * { box-sizing: border-box; margin: 0; padding: 0; }
  html, body { width: 1200px; height: 768px; overflow: hidden; }
  body {
    background: var(--bg);
    font-family: "Libre Baskerville", Georgia, serif;
    position: relative;
  }
  .card {
    position: absolute;
    top: 234px;
    width: 520px;
    height: 300px;
    background: var(--card);
    border-radius: 3px;
    overflow: hidden;
  }
  .card-back { left: 60px; }
  .card-front { left: 620px; }

  /* Back side */
  .company {
    position: absolute; top: 26px; left: 0; right: 0;
    text-align: center; color: var(--gold);
    font-weight: 700; font-size: 20px;
  }
  .tagline {
    position: absolute; top: 58px; left: 0; right: 0;
    text-align: center; color: var(--white);
    font-family: "Dancing Script", cursive; font-size: 19px;
  }
  .concepts {
    position: absolute; top: 98px; left: 40px; right: 40px;
    display: flex; justify-content: space-between;
  }
  .concept { width: 130px; text-align: center; }
  .concept-disc {
    width: 92px; height: 92px; margin: 0 auto;
    border-radius: 50%; background: var(--disc);
    display: flex; align-items: center; justify-content: center;
    box-shadow: 0 0 14px rgba(255,255,255,.25);
    font-size: 22px; color: var(--ink);
    text-align: center; line-height: 1.2;
  }
  .concept-disc.is-ringed { border: 3px solid var(--ring); }
  .concept-disc.is-small { font-size: 14px; padding: 0 10px; }
  .concept-address {
    margin-top: 12px; color: var(--white); font-size: 11px;
  }
  .contact-band {
    position: absolute; left: 0; right: 0; bottom: 0; height: 56px;
    background: var(--gold); color: var(--ink);
    display: flex; align-items: center; justify-content: center;
    font-size: 13px; gap: 12px;
  }

  /* Front side */
  .brand {
    position: absolute; top: 52px; left: 0; right: 0;
    text-align: center; color: var(--logo-gold);
    font-size: 50px; letter-spacing: 2px;
  }
  .holder {
    position: absolute; top: 170px; left: 180px;
    color: var(--gold); font-weight: 700; font-size: 24px;
  }
  .contact-list {
    position: absolute; top: 212px; left: 180px;
    list-style: none; color: var(--white); font-size: 14px;
  }
  .contact-list li { display: flex; align-items: center; gap: 10px; line-height: 24px; }
  .contact-list svg { width: 12px; height: 12px; fill: var(--gold); flex: none; }
</style>
</head>
<body>
  <section class="card card-back">
    <h1 class="company">Keystone Ventures, LLC</h1>
    <p class="tagline">Concepts by Dana Pruitt</p>
    <div class="concepts">
      <div class="concept">
        <div class="concept-disc">Pell</div>
        <p class="concept-address">1480 W Larkin Ave.</p>
      </div>
      <div class="concept">
        <div class="concept-disc">Rook</div>
        <p class="concept-address">1476 W Larkin Ave.</p>
      </div>
      <div class="concept">
        <div class="concept-disc is-ringed is-small">The Pruitt Room</div>
        <p class="concept-address">Coming Soon.</p>
      </div>
    </div>
    <div class="contact-band">
      <span>850-492-3106</span><span>|</span><span>dana@harborlampkitchen.example</span>
    </div>
  </section>

  <section class="card card-front">
    <div class="brand">HARBOR</div>
    <h2 class="holder">Dana Pruitt</h2>
    <ul class="contact-list">
      <li><svg viewBox="0 0 12 12" aria-hidden="true"><path d="M2 1h3l1 3-1.5 1a7 7 0 0 0 2.5 2.5L8 6l3 1v3a1 1 0 0 1-1 1A9 9 0 0 1 1 2a1 1 0 0 1 1-1z"/></svg>850-318-4672</li>
      <li><svg viewBox="0 0 12 12" aria-hidden="true"><path d="M1 2h10v8H1z M1 2l5 4 5-4" stroke="#0b0b0c" stroke-width=".8"/></svg>dana@harborlampkitchen.example</li>
      <li><svg viewBox="0 0 12 12" aria-hidden="true"><circle cx="6" cy="6" r="5"/><path d="M1 6h10M6 1v10" stroke="#0b0b0c" stroke-width=".8"/></svg>www.harborlampkitchen.example</li>
    </ul>
  </section>
</body>
</html>
```